Stella Marina packaging design

Hi there,
I'm trying to get an outstanding and unique design for my new product.I'm in baby products business.We are launching an organic,100% burp cloth for our online store. The packaging design is very important to our business.We are looking for something simple and unique.Our brand name is Stella Marina which means Sea Star in Italian. We also have dolphin prints on the burp cloth. Our burp cloth made of organic, hypoallergenic, breathable and ultra soft 100% cotton.Each box has 5 burp cloth. Its made with love and care for delicate and sensitive baby skin.I will attach samples of the burp cloth colors for you to get an idea about the product.

baby product

• Our Logo, ORVA image , and made of organic, hypoallergenic, breathable and ultra soft 100% cotton,has 5 burp cloth. Its made with love and care for delicate and sensitive baby skin.I will attach samples of the burp cloth colors for you to get an idea about the product.
• We are looking for something different and can Standout , please to don't make design that has the exact idea of the template that I provide.

```html
<!DOCTYPE html>
<html lang="en">
<head>
<meta charset="utf-8">
<title>Stella Marina – Baby Burp Cloth Box Dieline</title>
<link rel="stylesheet" href="https://fonts.googleapis.com/css2?family=Baloo+2:wght@600;700;800&family=Fira+Sans:ital,wght@0,400;0,500;1,400;1,500&display=swap">
<style>
  :root {
    --canvas: #e6e6e6;
    --paper: #ffffff;
    --green: #006633;
    --maroon: #994c4c;
    --maroon-deep: #8e3f3f;
    --brown-line: #6b2e2e;
    --blush: #f7f1f1;
    --ink: #1a1a1a;
    --side-ink: #3a2424;
  }
  html, body {
    margin: 0;
    padding: 0;
    width: 1200px;
    height: 1200px;
    overflow: hidden;
    background: var(--canvas);
  }
  .dieline { display: block; width: 1200px; height: 1200px; }
  .cut { stroke: #222; stroke-width: 1; }
  .headline { font-family: "Baloo 2", sans-serif; font-weight: 800; fill: var(--paper); }
  .brand { font-family: "Baloo 2", sans-serif; font-weight: 800; }
  .tagline { font-family: "Fira Sans", sans-serif; font-style: italic; font-weight: 400; fill: var(--paper); }
  .side-copy { font-family: "Fira Sans", sans-serif; font-weight: 400; fill: var(--side-ink); font-size: 11.5px; }
  .count-num { font-family: "Baloo 2", sans-serif; font-weight: 800; fill: var(--paper); }
  .count-label { font-family: "Fira Sans", sans-serif; fill: var(--paper); }
  .eco { font-family: "Fira Sans", sans-serif; font-style: italic; font-weight: 500; fill: var(--paper); }
  .eco-note { font-family: "Fira Sans", sans-serif; font-weight: 400; fill: var(--paper); }
</style>
</head>
<body>
<svg class="dieline" viewBox="0 0 1263 1263" xmlns="http://www.w3.org/2000/svg">
  <defs>
    <linearGradient id="panel-fade" x1="0" y1="0" x2="0" y2="1">
      <stop offset="0" stop-color="#ffffff"/>
      <stop offset="0.35" stop-color="#ecdcdc"/>
      <stop offset="0.7" stop-color="#b88080"/>
      <stop offset="1" stop-color="#8e3f3f"/>
    </linearGradient>
    <linearGradient id="wave-fade" x1="0" y1="0" x2="0" y2="1">
      <stop offset="0" stop-color="#b27272"/>
      <stop offset="1" stop-color="#8a3a3a"/>
    </linearGradient>
  </defs>

  <rect x="1" y="1" width="1261" height="1261" fill="var(--canvas)" stroke="#222" stroke-width="2"/>

  <!-- left side panel -->
  <g class="side-panel side-left">
    <rect class="cut" x="77" y="399" width="66" height="42" fill="var(--paper)"/>
    <rect class="cut" x="77" y="854" width="66" height="42" fill="var(--paper)"/>
    <rect class="cut" x="77" y="441" width="66" height="413" fill="url(#panel-fade)"/>
    <circle cx="110" cy="467" r="16" fill="var(--green)"/>
    <text class="count-num" x="110" y="474" font-size="20" text-anchor="middle">5</text>
    <text class="count-label" x="110" y="479" font-size="3.5" text-anchor="middle">Burp Cloth</text>
    <g transform="translate(110 640) rotate(-90)">
      <text class="side-copy" y="-13" text-anchor="middle">Super absorbent</text>
      <text class="side-copy" y="1" text-anchor="middle">Made with love for little ones</text>
      <text class="side-copy" y="15" text-anchor="middle">Suitable for baby delicate sensitive skin</text>
    </g>
    <g transform="translate(110 805) rotate(-90)">
      <text class="brand" y="-2" font-size="14" fill="var(--paper)" text-anchor="middle">Stella</text>
      <text class="brand" y="11" font-size="14" fill="var(--paper)" text-anchor="middle">Marina</text>
    </g>
  </g>

  <!-- back panel -->
  <rect class="cut back-panel" x="143" y="441" width="468" height="413" fill="var(--green)"/>

  <!-- right side panel -->
  <g class="side-panel side-right">
    <rect class="cut" x="611" y="399" width="66" height="42" fill="var(--paper)"/>
    <rect class="cut" x="611" y="854" width="66" height="42" fill="var(--paper)"/>
    <rect class="cut" x="611" y="441" width="66" height="413" fill="url(#panel-fade)"/>
    <circle cx="643" cy="467" r="16" fill="var(--green)"/>
    <text class="count-num" x="643" y="474" font-size="20" text-anchor="middle">5</text>
    <text class="count-label" x="643" y="479" font-size="3.5" text-anchor="middle">Burp Cloth</text>
    <g transform="translate(644 640) rotate(90)">
      <text class="side-copy" y="-10" text-anchor="middle">Super absorbent</text>
      <text class="side-copy" y="4" text-anchor="middle">Made with love for little ones</text>
      <text class="side-copy" y="18" text-anchor="middle">Suitable for baby delicate sensitive skin</text>
    </g>
    <g transform="translate(644 805) rotate(90)">
      <text class="brand" y="-2" font-size="14" fill="var(--paper)" text-anchor="middle">Stella</text>
      <text class="brand" y="11" font-size="14" fill="var(--paper)" text-anchor="middle">Marina</text>
    </g>
  </g>

  <!-- top lid and tuck flap -->
  <g class="top-lid">
    <rect class="cut" x="677" y="343" width="469" height="33" fill="var(--paper)"/>
    <rect class="cut" x="677" y="376" width="469" height="65" fill="var(--paper)"/>
    <g transform="translate(911 405) rotate(180)">
      <text class="brand" y="-8" font-size="26" fill="var(--ink)" text-anchor="middle">Stella</text>
      <text class="brand" y="16" font-size="26" fill="var(--ink)" text-anchor="middle">Marina</text>
    </g>
  </g>

  <!-- glue flap -->
  <g class="glue-flap">
    <rect class="cut" x="1146" y="441" width="40" height="413" fill="var(--paper)"/>
    <line class="cut" x1="1179" y1="441" x2="1179" y2="854"/>
  </g>

  <!-- bottom flap -->
  <g class="bottom-flap">
    <rect class="cut" x="677" y="854" width="469" height="65" fill="var(--maroon)"/>
    <text class="brand" x="911" y="884" font-size="27" fill="var(--paper)" text-anchor="middle">Stella</text>
    <text class="brand" x="911" y="910" font-size="27" fill="var(--paper)" text-anchor="middle">Marina</text>
  </g>

  <!-- front panel -->
  <g class="front-panel">
    <rect class="cut" x="677" y="441" width="469" height="413" fill="url(#panel-fade)"/>

    <rect class="leaf-ornament" role="img" aria-label="Green leaf swirl ornament" x="682" y="445" width="155" height="50" rx="25" fill="var(--green)" opacity="0.85"/>
    <rect class="leaf-ornament" role="img" aria-label="Green leaf swirl ornament" x="985" y="445" width="155" height="50" rx="25" fill="var(--green)" opacity="0.85"/>

    <path class="window-frame" d="M750,805 V530 Q750,505 775,505 H843 M979,505 H1050 Q1075,505 1075,530 V805" fill="none" stroke="var(--brown-line)" stroke-width="4"/>
    <circle class="brand-seal" cx="911" cy="515" r="68" fill="var(--blush)" stroke="var(--brown-line)" stroke-width="4"/>
    <text class="brand" x="911" y="522" font-size="17" fill="var(--brown-line)" text-anchor="middle">Stella Marina</text>

    <rect class="title-band" x="677" y="603" width="469" height="94" fill="var(--green)"/>
    <text class="headline" x="911" y="654" font-size="56" text-anchor="middle">Baby Burp Cloth</text>
    <text class="tagline" x="911" y="686" font-size="19" text-anchor="middle">Ultra-Soft, breathable, Hypoallergenic</text>

    <rect class="wave-ornament" role="img" aria-label="Flowing white wave swirl ornament"
      x="678" y="760" width="467" height="93" fill="url(#wave-fade)"/>

    <circle class="cert-badge" cx="711" cy="733" r="22" fill="var(--green)" stroke="var(--paper)" stroke-width="2"/>

    <circle class="count-badge" cx="1110" cy="731" r="23" fill="var(--green)" stroke="var(--paper)" stroke-width="2"/>
    <text class="count-num" x="1110" y="741" font-size="30" text-anchor="middle">5</text>
    <text class="count-label" x="1110" y="747" font-size="5" text-anchor="middle">Burp Cloth</text>

    <text class="eco" x="1000" y="826" font-size="18" text-anchor="middle">Eco-friendly</text>
    <text class="eco-note" x="988" y="843" font-size="12" text-anchor="middle">100% certified organic cotton</text>
  </g>
</svg>
</body>
</html>
```